Security Camera Sign

14” high x 11” wide Color: Blue, Yellow, Black and white

Make the sign vertical
Replace red with blue
WARNING: Black over yellow
These premises are protected by Closed Circuit Television: On white
Images are recorded for crime prevention and public safety. Unauthorized access, theft or vandalism will result in prosecution: On Blue

Target Market(s)

Outdoor commercial building

Industry/Entity Type

Security

Requirements
Nice to have
• I would like the sign stand out. If you need more colors? Thanks Ok

```html
<!DOCTYPE html>
<html lang="en">
<head>
<meta charset="utf-8">
<title>Security Camera Sign</title>
<link rel="stylesheet" href="https://fonts.googleapis.com/css2?family=Open+Sans:wght@700&display=swap">
<style>
  :root {
    --backdrop: #d2d3d5;
    --sign-blue-light: #1a7bc3;
    --sign-blue-dark: #0e5894;
    --warning-yellow: #fff200;
    --ink: #0a0a0a;
    --paper: #ffffff;
    --camera-tone: #1c1c1c;
    --camera-accent: #1672bd;
  }
  * { box-sizing: border-box; margin: 0; padding: 0; }
  html, body {
    width: 1200px;
    height: 938px;
    overflow: hidden;
    background: var(--backdrop);
    font-family: "Open Sans", Arial, sans-serif;
  }
  .canvas {
    position: relative;
    width: 1200px;
    height: 938px;
  }
  .sign {
    position: absolute;
    left: 301px;
    top: 84px;
    width: 598px;
    height: 760px;
    border-radius: 28px;
    border: 2px solid var(--ink);
    background: linear-gradient(90deg, var(--sign-blue-light), var(--sign-blue-dark));
    overflow: hidden;
    box-shadow: 0 14px 10px -8px rgba(0,0,0,0.35);
  }
  .warning-bar {
    position: absolute;
    left: 38px;
    top: 30px;
    width: 518px;
    height: 96px;
    background: var(--warning-yellow);
    border: 3px solid var(--ink);
    border-radius: 9px;
    display: flex;
    align-items: center;
    justify-content: center;
  }
  .warning-title {
    font-weight: 700;
    font-size: 84px;
    line-height: 1;
    color: var(--ink);
    margin-top: 4px;
  }
  .notice-panel {
    position: absolute;
    left: 0;
    top: 154px;
    width: 100%;
    height: 470px;
    background: var(--paper);
  }
  .camera-art {
    position: absolute;
    left: 162px;
    top: 26px;
    width: 270px;
    height: 190px;
    border-radius: 12px;
    background: linear-gradient(135deg, #2a2a2a, var(--camera-tone) 70%, var(--camera-accent));
  }
  .notice-text {
    position: absolute;
    left: 0;
    top: 238px;
    width: 100%;
    text-align: center;
    font-weight: 700;
    font-size: 32px;
    line-height: 35px;
    color: var(--ink);
  }
  .footer-text {
    position: absolute;
    left: 30px;
    top: 640px;
    width: 534px;
    font-weight: 700;
    font-size: 19.5px;
    line-height: 26px;
    color: var(--paper);
    text-align: justify;
    text-align-last: left;
  }
</style>
</head>
<body>
<div class="canvas">
  <div class="sign">
    <div class="warning-bar">
      <h1 class="warning-title">WARNING</h1>
    </div>
    <div class="notice-panel">
      <div class="camera-art" role="img" aria-label="Illustration of a wall-mounted CCTV security camera"></div>
      <p class="notice-text">THESE<br>PREMISES ARE<br>PROTECTED<br>BY CLOSED<br>CIRCUIT<br>TELEVISION</p>
    </div>
    <p class="footer-text">IMAGES ARE RECORDED FOR CRIME PREVENTION AND PUBLIC SAFETY. UNAUTHORIZED ACCESS, THEFT OR VANDALISM WILL RESULT IN PROSECUTION</p>
  </div>
</div>
</body>
</html>
```